Create New Bussiness Card For New Shoes Store

Vandrule is a store that sells a variety of skateboard shoes such as Kestro, Mollen etc. we also sell some skateboard and all skateboard accessories.
we like black and white style logo, but also like blue as well.
We are fully assembled with a deck, truck, wheels, and bearings. Add some personality to your board with a fun, graphic skateboard deck. Constructed of thick 7 ply maple,
Target Market(s)
Target audience: 12-40 year old
especially for young man
Industry/Entity Type
Industrial
Contact Information for Business Card
Name: Vandrule
Address1: 2483 Harlow Brisket Rd
City: Xenia
State: Ohio
Zip: 45385
Country: US
Phone: 614830296
email: markolvenby@plimmail.test

```html
<!DOCTYPE html>
<html lang="en">
<head>
<meta charset="utf-8">
<title>Vandrule Business Card</title>
<link rel="stylesheet" href="https://fonts.googleapis.com/css2?family=Source+Sans+3:wght@400;600&display=swap">
<style>
  :root {
    --brand-blue: #1e5bb8;
    --paper: #ffffff;
    --ink: #141414;
    --backdrop: #ecebe8;
    --edge: rgba(0, 0, 0, 0.2);
  }
  * { box-sizing: border-box; margin: 0; padding: 0; }
  html, body {
    width: 1200px;
    height: 900px;
    overflow: hidden;
    background: var(--backdrop);
    font-family: "Source Sans 3", "Myriad Pro", sans-serif;
  }
  .card {
    position: absolute;
    width: 640px;
    height: 366px;
    box-shadow: 0 10px 28px var(--edge);
  }
  .card-back {
    left: 80px;
    top: 70px;
    background: var(--ink);
    display: flex;
    align-items: center;
    justify-content: center;
  }
  .card-front {
    left: 480px;
    top: 464px;
    background: var(--paper);
  }
  .wordmark {
    display: flex;
    align-items: center;
    gap: 14px;
    font-weight: 400;
    font-size: 50px;
    letter-spacing: 1px;
    line-height: 1;
  }
  .wordmark-dot {
    width: 18px;
    height: 18px;
    border-radius: 50%;
    background: var(--brand-blue);
  }
  .card-back .wordmark { color: var(--paper); }
  .card-front .wordmark {
    position: absolute;
    left: 50px;
    top: 140px;
    color: var(--ink);
    font-size: 46px;
  }
  .contact-block {
    position: absolute;
    left: 380px;
    top: 104px;
    color: var(--ink);
    font-size: 15px;
    line-height: 1.3;
  }
  .person-name {
    color: var(--brand-blue);
    font-weight: 600;
    font-size: 20px;
    line-height: 1.1;
  }
  .person-role { margin-bottom: 14px; }
  .address { margin-bottom: 14px; padding-left: 14px; }
  .contact-list { list-style: none; padding-left: 14px; }
  .contact-list li {
    display: flex;
    align-items: center;
    gap: 10px;
    margin-bottom: 2px;
  }
  .contact-icon {
    width: 13px;
    height: 13px;
    fill: var(--brand-blue);
    flex: none;
  }
  .contact-icon.link-icon {
    fill: none;
    stroke: var(--brand-blue);
    stroke-width: 1.8;
    stroke-linecap: round;
  }
</style>
</head>
<body>
  <section class="card card-back">
    <div class="wordmark">
      <span class="wordmark-dot"></span>
      <span class="wordmark-name">Vandrule</span>
    </div>
  </section>

  <section class="card card-front">
    <div class="wordmark">
      <span class="wordmark-dot"></span>
      <span class="wordmark-name">Vandrule</span>
    </div>

    <div class="contact-block">
      <p class="person-name">Mark Olvenby</p>
      <p class="person-role">Managing Director</p>
      <p class="address">2483 Harlow Brisket Rd<br>Xenia, Ohio 45385, US</p>
      <ul class="contact-list">
        <li>
          <svg class="contact-icon" viewBox="0 0 16 16" aria-hidden="true"><path d="M3.6 1l2.2 3.1-1.3 1.5c.8 2 2.3 3.5 4.3 4.3l1.5-1.3L13.4 10.8 12.3 13.6C7 14 2 9 2.4 3.7z"/></svg>
          <span>614830296</span>
        </li>
        <li>
          <svg class="contact-icon" viewBox="0 0 16 16" aria-hidden="true"><path d="M1 3h14v10H1z M2.2 4.2L8 8.6l5.8-4.4z" fill-rule="evenodd"/></svg>
          <span>markolvenby@plimmail.test</span>
        </li>
        <li>
          <svg class="contact-icon link-icon" viewBox="0 0 16 16" aria-hidden="true"><path d="M6.5 9.5l3-3M5 7.5L3.3 9.2a2.3 2.3 0 003.3 3.3L8.3 10.8M11 8.5l1.7-1.7a2.3 2.3 0 00-3.3-3.3L7.7 5.2"/></svg>
          <span>www.vandrule.test</span>
        </li>
      </ul>
    </div>
  </section>
</body>
</html>
```